Tallowfen Capital Group - letterhead

We need a corporate letterhead template (word) and slide show template (PowerPoint) designed for our investment business Tallowfen Capital Group.

Tallowfen Capital Group manages a group of investments in Australia and are after a letterhead template and PowerPoint template that is both creative and professional in design.

Information to be included on the letterhead (word) template is as follows:

Level 4, 318 Marlow Road
Kew VIC 3101

t. 03 5127 6618

Please feel free to ask any questions.

Investment

```html
<!DOCTYPE html>
<html lang="en">
<head>
<meta charset="utf-8">
<title>Tallowfen Capital Group – Slide Template</title>
<link href="https://fonts.googleapis.com/css2?family=Carlito:ital,wght@0,400;0,700;1,400&display=swap" rel="stylesheet">
<style>
  :root {
    --brand-blue: #0066a3;
    --accent-grey: #b3b3b3;
    --text-dark: #333333;
    --page-bg: #e6e7e9;
    --slide-bg: #ffffff;
  }
  * { margin: 0; padding: 0; box-sizing: border-box; }
  html, body {
    width: 1200px;
    height: 812px;
    overflow: hidden;
    background: var(--page-bg);
    font-family: "Carlito", "Calibri", sans-serif;
  }
  .slide {
    position: absolute;
    left: 100px;
    top: 31px;
    width: 1000px;
    height: 749px;
    background: var(--slide-bg);
    box-shadow: 0 4px 14px rgba(0, 0, 0, 0.25);
    overflow: hidden;
  }
  .brand-name {
    position: absolute;
    left: 100px;
    top: 62px;
    font-size: 32px;
    font-weight: 400;
    color: var(--brand-blue);
    letter-spacing: 0.5px;
  }
  .corner-band {
    position: absolute;
    right: 0;
    top: 0;
    width: 205px;
    height: 118px;
    background: var(--brand-blue);
  }
  .slide-title {
    position: absolute;
    left: 160px;
    top: 196px;
    font-size: 35px;
    font-weight: 700;
    color: var(--brand-blue);
  }
  .title-rule {
    position: absolute;
    left: 125px;
    top: 248px;
    width: 458px;
    height: 1px;
    background: var(--brand-blue);
  }
  .slide-body {
    position: absolute;
    left: 152px;
    top: 276px;
    width: 790px;
    font-size: 24px;
    line-height: 26px;
    font-style: italic;
    color: var(--text-dark);
  }
  .footer-band {
    position: absolute;
    left: 0;
    bottom: 0;
    width: 100%;
    height: 33px;
    display: flex;
  }
  .footer-band .footer-accent { width: 150px; background: var(--accent-grey); }
  .footer-band .footer-main { flex: 1; background: var(--brand-blue); }
</style>
</head>
<body>
  <main class="slide">
    <div class="brand-name">Tallowfen Capital Group</div>
    <div class="corner-band"></div>
    <h1 class="slide-title">Introduction</h1>
    <div class="title-rule"></div>
    <p class="slide-body">Ut scelerisque viverra ligula, ut euismod lectus varius eget. Maecenas non pharetra neque. Suspendisse potenti. Donec eget mauris et ligula ullamcorper laoreet. Donec tristique dapibus lacus, nec blandit dui dignissim pharetra. Maecenas vulputate est eget blandit euismod. Sed et dolor venenatis, tempus lorem in, aliquet metus. Nunc eu orci vel metus molestie porta.</p>
    <div class="footer-band">
      <div class="footer-accent"></div>
      <div class="footer-main"></div>
    </div>
  </main>
</body>
</html>
```